2 Fold Brochure

We are a spa looking to create a professional elegant two fold brochure for a spa mainly black and white with a splash of lime green.
Look and feel: chic, modern, and spa-ish.

The front will include an image and also it should say: (somewhere under the photo) wherever you think it will look nice.
Skin Tightening
Cellulite Reduction
Body Contouring

The second Page:
Bipolar Radiofrequency(bolded): for immediate face lifting, tone and a complete new younger looking skin!
Multipolar Radiofrequency(bolded): with Vacuum system for body contour, cellulite and fat detachment from adipose tissue.
Cavitation with red LED to treat face and small areas of the body. Red LED light stimulates collagen synthesis.

Ultra Cavitation will sculpt, treat fat, cellulite and improve body shape! It does NOT involve surgery. There is no need for anesthesia, hospital stay or time off from work. Ultra cavitation will promote microscopic air bubbles to surround the lipocyte(fat cell) membranes and with its resonant frequency, the bubbles cause a high enough pressure to break up fat instantly. These broken lipocytes are then safely metabolized out of the human body.

PRESSOTHERAPY: A Complete Body Detox! Pressortherapy based on air pressure, promotes lymphatic drainage. It aslo has infrared system for body heat and electro muscle stimulation system.

Third Page:
Packages:

1. THE NEW FACELIFT:
*Skin Tightening
*Wrinkle Reduction
*Dark Circle Elimination
*Puffy Eye Relief

BODY SHAPING

2. BODY
*Fat Reduction
*Cellulite Reduction
*Body Firming

3. PRESSOTHERAPY (DETOX) $85
*Toxic Flushing
*Lymphatic Drainage
*Toning

5.POST PREGNANCY
*Fat Reduction
*Tummy Firming and Toning
*Cellulite Reduction
*Butt Toning

Buy 5 get 1 Free - $1,250
Buy 10 get 2 Free- $2,500

The back of the second page will include before and after photos I will be sending later. Also include the Logo in the front and by the prices. I have attached our logo.

Also we need a photo to place in the front. Something that shows face and body fat reduction.

```html
<!DOCTYPE html>
<html lang="en">
<head>
<meta charset="utf-8">
<title>Spa Treatments Brochure Panel</title>
<link href="https://fonts.googleapis.com/css2?family=Open+Sans:wght@400;600;700;800&display=swap" rel="stylesheet">
<style>
  :root {
    --lime: #8cc63f;
    --ink: #3d3d3d;
    --ink-strong: #1e1e1e;
    --band: #0a0a0a;
    --paper: #ffffff;
    --rule: #9a9a9a;
  }
  * { margin: 0; padding: 0; box-sizing: border-box; }
  html, body { width: 1200px; height: 2914px; overflow: hidden; background: var(--paper); }
  body { font-family: "Open Sans", Arial, sans-serif; color: var(--ink); }

  .panel { position: relative; width: 1200px; height: 2914px; }

  .hero-photo {
    position: absolute; left: 0; top: 0; width: 1200px; height: 770px;
    background: linear-gradient(160deg, #f4eee8 0%, #e9d7c8 40%, #d8bca6 65%, #f2ece6 100%);
  }

  .treatment-columns {
    position: absolute; left: 60px; top: 800px; width: 1110px; height: 420px;
    display: flex;
  }
  .treatment { flex: 1; }
  .treatment--left { padding-right: 40px; }
  .treatment--right { padding-left: 36px; border-left: 3px solid var(--rule); }
  .treatment-title {
    color: var(--lime); font-weight: 700; font-size: 56px; line-height: 60px;
    letter-spacing: -0.5px; margin-bottom: 8px;
  }
  .treatment-text { font-size: 35px; line-height: 44px; }
  .treatment-text strong { color: var(--ink-strong); font-weight: 700; }

  .cavitation {
    position: absolute; left: 60px; top: 1240px; width: 1100px;
  }
  .cavitation .treatment-title { margin-bottom: 2px; }

  .info-band {
    position: absolute; left: 0; top: 1395px; width: 1200px; height: 545px;
    background: var(--band); color: var(--paper);
    padding: 52px 48px 0 58px;
    font-size: 33px; line-height: 44px;
  }

  .detox {
    position: absolute; left: 60px; top: 1975px; width: 1100px;
  }
  .detox-title {
    color: var(--lime); font-weight: 700; font-size: 64px; line-height: 70px;
    letter-spacing: -0.5px;
  }
  .detox-text { font-size: 36px; line-height: 44px; }

  .relax-photo {
    position: absolute; left: 0; top: 2235px; width: 1200px; height: 679px;
    background: linear-gradient(180deg, #f6f2ee 0%, #e6d5c6 45%, #d3b49c 75%, #ead8ce 100%);
  }
</style>
</head>
<body>
<main class="panel">
  <div class="hero-photo" role="img" aria-label="Close-up of a relaxed woman with a white towel wrap receiving a gentle facial treatment"></div>

  <section class="treatment-columns">
    <div class="treatment treatment--left">
      <h2 class="treatment-title">Bipolar Radiofrequency</h2>
      <p class="treatment-text">for immediate face lifting, tone and a&nbsp; complete new <strong>younger looking skin!</strong></p>
    </div>
    <div class="treatment treatment--right">
      <h2 class="treatment-title">Multipolar Radiofrequency</h2>
      <p class="treatment-text">with Vacuum system for body contour, cellulite and fat detachment from adipose tissue.</p>
    </div>
  </section>

  <section class="cavitation">
    <h2 class="treatment-title">Cavitation with red LED</h2>
    <p class="treatment-text">to treat face and small areas of the body. Red LED light stimulates collagen synthesis</p>
  </section>

  <section class="info-band">
    <p>Ultra Cavitation will sculpt, treat fat, cellulite and improve body shape! It does NOT involve surgery. There is no need for anesthesia, hospital stay or time off from work. Ultra cavitation will promote microscopic air bubbles to surround the lipocyte(fat cell) membranes and with its resonant frequency, the bubbles cause a high enough pressure to break up fat instantly. These broken lipocytes are then safely metabolized out of the human body.</p>
  </section>

  <section class="detox">
    <h2 class="detox-title">PRESSOTHERAPY:</h2>
    <p class="detox-text">A Complete Body Detox! Pressortherapy based on air pressure, promotes lymphatic drainage. It aslo has infrared system for body heat and electro muscle stimulation system.</p>
  </section>

  <div class="relax-photo" role="img" aria-label="Woman lying face down on a spa table with pink orchid flowers in the foreground"></div>
</main>
</body>
</html>
```